Simple, elegant, business card design required

Hi designers,I am looking for a simple yet elegant business card design.

Please make use of my logo (attached); you are free to tweak the logo should you wish to do so.

Our business is involved in many different fields - almost all of them involved in some form of "design", so that's really one of the key things I want to portray. I do not wish to specify which field of design, exactly.

I prefer white on black (or just monochromatic), but if you have a different, creative idea, I am open to that too.

You can use artsy photographs provided that you have the license to use those. Please feel free to ask me any questions.
Updates

Project Deadline Extended Reason: Small extension for potential revisions. Did not get the time to provide as much feedback as I can. Added Wednesday, July 09, 2014

Target Market(s)

High-end customers looking for design consultancy

Industry/Entity Type

Business

Contact Information for Business Card

Name: Gareth Moonfield
Position: Creative Director
Mobile: +155603928174
Address: Barrow Lane, Elmbridge Vale, Harrowdale GL12 4RT
Website: torvakest.com (not launched yet)

Requirements
Must have
• Design layout must be clean, original, and text must be readable when printed.
Should not have
• ~ No business card templates please. Anyone using this will be reported.
• ~ Please don't spam entries.

```html
<!DOCTYPE html>
<html lang="en">
<head>
<meta charset="utf-8">
<title>Torvakest — Business Card</title>
<link rel="stylesheet" href="https://fonts.googleapis.com/css2?family=Mako&display=swap">
<style>
  :root {
    --page-bg: #ffffff;
    --card-black: #000000;
    --panel-light: #7a7b7d;
    --panel-dark: #3c3c3d;
    --text-white: #ffffff;
    --accent-lime: #b7cc2f;
    --edge-shine: #d8d8d8;
  }
  html, body {
    margin: 0;
    padding: 0;
    width: 1200px;
    height: 1000px;
    overflow: hidden;
    background: var(--page-bg);
  }
  .canvas {
    position: relative;
    width: 1200px;
    height: 1000px;
    font-family: "Mako", "Helvetica Neue", Arial, sans-serif;
  }
  .business-card {
    position: absolute;
    left: 88px;
    top: 211px;
    width: 1003px;
    height: 553px;
    background: var(--card-black);
    box-shadow: 6px 8px 8px rgba(0, 0, 0, 0.28);
    overflow: hidden;
  }
  .card-shapes {
    position: absolute;
    inset: 0;
  }
  .holder {
    position: absolute;
    left: 100px;
    color: var(--text-white);
    margin: 0;
    white-space: nowrap;
  }
  .holder-name {
    top: 88px;
    font-size: 41px;
    font-weight: 400;
    line-height: 1;
  }
  .holder-role {
    top: 136px;
    font-size: 31px;
    color: var(--accent-lime);
    line-height: 1;
  }
  .contact-list {
    position: absolute;
    left: 100px;
    top: 340px;
    margin: 0;
    padding: 0;
    list-style: none;
    font-size: 26px;
    line-height: 30px;
    color: var(--text-white);
    white-space: nowrap;
  }
  .contact-label {
    color: var(--accent-lime);
  }
  .brand {
    position: absolute;
    left: 636px;
    top: 252px;
    display: flex;
    align-items: center;
    gap: 36px;
  }
  .brand-mark {
    width: 58px;
    height: 58px;
    border: 5px solid var(--text-white);
    border-radius: 50%;
    box-sizing: border-box;
  }
  .brand-name {
    font-size: 30px;
    letter-spacing: 7px;
    color: var(--text-white);
    line-height: 1;
  }
</style>
</head>
<body>
<div class="canvas">
  <section class="business-card" aria-label="Business card">
    <svg class="card-shapes" width="1003" height="553" viewBox="0 0 1003 553" aria-hidden="true">
      <defs>
        <linearGradient id="panelFill" x1="1" y1="0" x2="0" y2="1">
          <stop offset="0" stop-color="#7a7b7d"/>
          <stop offset="1" stop-color="#3c3c3d"/>
        </linearGradient>
        <linearGradient id="edgeFill" x1="0" y1="0" x2="0" y2="1">
          <stop offset="0" stop-color="#222"/>
          <stop offset="0.45" stop-color="#555"/>
          <stop offset="0.8" stop-color="#d8d8d8"/>
          <stop offset="1" stop-color="#ffffff"/>
        </linearGradient>
        <radialGradient id="panelSheen" cx="0.35" cy="0.2" r="0.7">
          <stop offset="0" stop-color="#ffffff" stop-opacity="0.12"/>
          <stop offset="1" stop-color="#ffffff" stop-opacity="0"/>
        </radialGradient>
      </defs>
      <polygon class="info-panel" points="30,0 504,0 574,553 30,553" fill="url(#panelFill)"/>
      <path class="panel-sheen" d="M30,0 L504,0 L518,205 C430,270 300,290 180,285 C110,282 60,270 30,255 Z" fill="url(#panelSheen)"/>
      <polygon class="panel-edge" points="504,0 508,0 585,553 574,553" fill="url(#edgeFill)"/>
    </svg>

    <h1 class="holder holder-name">Gareth Moonfield</h1>
    <p class="holder holder-role">Creative Director</p>

    <ul class="contact-list">
      <li><span class="contact-label">Mobile</span>+155603928174</li>
      <li><span class="contact-label">Address</span> Barrow Lane</li>
      <li>Elmbridge Vale</li>
      <li>Harrowdale GL12 4RT</li>
      <li><span class="contact-label">Website</span> torvakest.com</li>
    </ul>

    <div class="brand">
      <span class="brand-mark" aria-hidden="true"></span>
      <span class="brand-name">TORVAKEST</span>
    </div>
  </section>
</div>
</body>
</html>
```